Collectibles expert needs a new business card design.

My current business card makes me look to high end. It may even make me look arrogant or too stuffy. I do work with high end clients and their items but most of my business is with average people with average items. My business name is Walter Brennick's Oak Lane Digging Co. The idea was that I mine the streets helping people discover the treasures buried in their homes. That could be art, jewelry, coins, etc. The name and an older logo I used does not make immediate sense to most people. I tried to go with just my picture and name and that is the current card I am changing. I help people who need to downsize. Whether they are getting rid of one item, a collection or a house full of items I help them discover what they have, what it is worth and what are the best ways we can get the most for them. This may be a combination of estate sale (which I dont do) auction or sell directly to a dealer or collector. Usually it is a combination of these. My main goal is to help make sure they dont accidently sell a Vantorre painting in a garage sale. I am uploading a copy of my old card and the old logo I used to use but the winning card design will need to be much different than these. You can learn a little more about me at www.walterpbrennick.com, www.oaklanedigin.com and www.facebook.com/oldco. I hope someone can look at what I do and come up with a very unique design that will be equally effective if my client is high income or if my client is low to mid income. I do not care if it is a one or two sided card as long as it conveys my contact information and a good representation of what I do.

Target Market(s)

People who are getting rid of items. These can be elderly couples or individuals that are moving to an active living community and will have less space so they need to sell items. This can also include the children of elder parents that dont want their stuff and want to find solutions to help them get rid of their items.

Contact Information for Business Card

The card should have my business name Walter Brennick's Oak Lane Digging Co., phone number 555-382-19073, email walter@oaklanedigging.com and website www.oaklanedigging.com. Would also like to include Buyer, Broker, Consultant and Appraiser. We can put Walter P. Brennick, ISA on the opposite side of the company name since it includes my name as well.

Font styles to use
Sans Serif

Colors

Designer to choose colors to be used in the design.

Requirements
Must have
• My project must have a professional look. It must not alienate low income clients and should still be appealing to high value clients.

```html
<!DOCTYPE html>
<html lang="en">
<head>
<meta charset="utf-8">
<title>Walter Brennick's Business Card</title>
<link rel="stylesheet" href="https://fonts.googleapis.com/css2?family=Archivo:wght@500&family=Lato:wght@400&display=swap">
<style>
  :root {
    --canvas: #d9d9db;
    --card-white: #ffffff;
    --card-shade: #ebebeb;
    --ink: #3b1414;
    --ink-soft: #4a2222;
    --maroon: #6e1e1e;
    --maroon-dark: #2a0c0c;
    --denim: #86abcd;
    --photo-mid: #7a6a64;
    --photo-light: #efe9e6;
  }
  * { box-sizing: border-box; margin: 0; padding: 0; }
  html, body {
    width: 1200px; height: 900px; overflow: hidden;
    background: var(--canvas);
  }
  .stage {
    width: 1200px; height: 900px;
    display: flex; flex-direction: column; align-items: center; justify-content: center;
    gap: 60px;
  }
  .card {
    position: relative;
    width: 630px; height: 360px;
    border-radius: 22px;
    overflow: hidden;
    box-shadow: 0 10px 28px rgba(0,0,0,0.18);
  }
  .name {
    font-family: "Archivo", sans-serif;
    font-weight: 500;
    font-size: 28px;
    letter-spacing: 2px;
    text-transform: uppercase;
    color: var(--ink);
    line-height: 1.1;
  }
  .role {
    font-family: "Lato", sans-serif;
    font-size: 17px;
    color: var(--ink-soft);
    margin-top: 6px;
  }

  /* Front */
  .card-front {
    background: linear-gradient(160deg, var(--card-shade) 0%, var(--card-white) 55%);
  }
  .identity {
    position: absolute; left: 58px; top: 56px;
  }
  .rule {
    width: 26px; height: 2px; background: var(--ink);
    margin: 18px 0 14px;
  }
  .contact-list { list-style: none; }
  .contact-item {
    display: flex; align-items: center; gap: 10px;
    font-family: "Lato", sans-serif;
    font-size: 16px;
    color: var(--ink-soft);
    line-height: 27px;
  }
  .contact-item svg { width: 12px; height: 12px; flex: none; }
  .brand-block {
    position: absolute; right: 48px; bottom: 22px;
    width: 210px;
    display: flex; flex-direction: column; align-items: center; gap: 10px;
  }
  .illustration {
    width: 190px; height: 190px;
    border-radius: 10px;
    background: linear-gradient(135deg, var(--denim) 0%, #8a6e7c 45%, var(--maroon) 75%, var(--maroon-dark) 100%);
  }
  .company-name {
    font-family: "Archivo", sans-serif;
    font-weight: 500;
    font-size: 15px;
    letter-spacing: 1px;
    color: var(--ink);
    white-space: nowrap;
  }

  /* Back */
  .card-back {
    background: linear-gradient(100deg, var(--maroon-dark) 0%, var(--photo-mid) 42%, var(--photo-light) 72%, var(--card-white) 100%);
  }
  .portrait { position: absolute; inset: 0; }
  .back-identity {
    position: absolute; left: 255px; bottom: 68px;
  }
</style>
</head>
<body>
<main class="stage">
  <section class="card card-front" aria-label="Card front">
    <div class="identity">
      <h1 class="name">Walter Brennick's</h1>
      <p class="role">Buyer, Broker, Consultant</p>
      <div class="rule"></div>
      <ul class="contact-list">
        <li class="contact-item">
          <svg viewBox="0 0 12 12" aria-hidden="true"><path d="M3 1 L5 3.5 L4 5 Q5 7.5 7 8 L8.5 7 L11 9 L9.5 11 Q3 10 1 2.5 Z" fill="var(--ink)"/></svg>
          555-382-19073,
        </li>
        <li class="contact-item">
          <svg viewBox="0 0 12 12" aria-hidden="true"><rect x="1" y="2.5" width="10" height="7" fill="none" stroke="var(--ink)" stroke-width="1.2"/><path d="M1 2.5 L6 6.5 L11 2.5" fill="none" stroke="var(--ink)" stroke-width="1.2"/></svg>
          walter@oaklanedigging.com
        </li>
        <li class="contact-item">
          <svg viewBox="0 0 12 12" aria-hidden="true"><circle cx="6" cy="6" r="5" fill="none" stroke="var(--ink)" stroke-width="1.2"/><path d="M1 6 H11 M6 1 Q3 6 6 11 Q9 6 6 1" fill="none" stroke="var(--ink)" stroke-width="1"/></svg>
          www.oaklanedigging.com
        </li>
      </ul>
    </div>
    <div class="brand-block">
      <div class="illustration" role="img" aria-label="Illustration of a woman miner with a pickaxe sitting on a red mine cart full of gold"></div>
      <p class="company-name">Oak Lane Digging Co.</p>
    </div>
  </section>

  <section class="card card-back" aria-label="Card back">
    <div class="portrait" role="img" aria-label="Portrait photograph of the collectibles expert in a cap and glasses"></div>
    <div class="back-identity">
      <h2 class="name">Walter Brennick's</h2>
      <p class="role">Buyer, Broker, Consultant</p>
    </div>
  </section>
</main>
</body>
</html>
```